Create Homepage Header & Search Box for Education Website

This project is relatively small and pays well.
Site: brightvalelearning.org
Project Title:
Redesign slider to be a static image/graphic and include a 3 drop down search box.
Project Summary:
We need a new homepage header for brightvalelearning.org. The logo, top navigation, and social buttons should remain unchanged. The new header needs to include a static graphic or image and a 3 drop down search box. It can also include some text that speaks to the what our site provides. For text suggestions - see below. Placement for the search box should be to the left under the logo. We will remove the slider functionality and need the design to be static.
Below the current slider images are bar graphs and a pie graph. These can remain as is - or you can make design changes. If you make design changes - please be sure the message doesn't change. Also you can submit one version of the design with this removed if you feel like it helps best accomplish our goal of conversion.
Project Objectives:
The primary objective of the deign is to maximize conversion of clicks to the search box. We need users to gravitate to the search box. Additionally the design should convey trust and academic feel.
Target Market:
High School Graduates and people in their 20s looking for college options.
Potential text:
Tagline Option: "Your #1 Resource for an Affordable Online College Education"
Tagline Option: "Find Affordable Online College Options"
Other Details: Brightvale Learning Hub will help you find a more affordable college experience. Look no further to find financial aid information, cost saving tips, and comprehensive college rankings focused on affordability and value.
Or you can also use some placeholder text and I can create the right messaging.
The Search Box:
The search box is pretty standard - you can see examples in the examples below - or in the files I attached. 3 drop downs and a "Search" button.
Examples of some previous designs attached to the project:
These designs are close - but not perfect. These will give you a good general idea for what we need.
Examples of designs at similar websites:
kwpn.org
studyharborhub.net
topmeadowcourses.com

```html
<!DOCTYPE html>
<html lang="en">
<head>
<meta charset="utf-8">
<title>Brightvale Learning Hub – Home</title>
<link rel="stylesheet" href="https://fonts.googleapis.com/css2?family=Dosis:wght@400;500;600&family=Oswald:wght@500;600;700&family=Open+Sans:wght@400;600&display=swap">
<style>
  :root {
    --orange: #f26f3a;
    --orange-soft: #f59a76;
    --white: #ffffff;
    --ink: #231f20;
    --panel: #252122;
    --teal: #19a3a0;
    --teal-dark: #0e5a55;
    --navy: #101a1f;
    --navy-line: #24323a;
    --headline-dark: #2a1a14;
    --photo-light: #e37a55;
    --photo-mid: #c9573e;
    --photo-dark: #8f3d31;
    --grey: #7b7b7b;
  }
  * { box-sizing: border-box; margin: 0; padding: 0; }
  html, body { width: 1200px; height: 689px; overflow: hidden; background: var(--white); }
  .header { position: relative; width: 1200px; height: 689px; overflow: hidden; font-family: "Dosis", sans-serif; }

  .top-bar { position: absolute; left: 0; top: 0; width: 1200px; height: 77px; background: var(--white); }
  .brand { position: absolute; left: 102px; top: 18px; display: flex; align-items: center; gap: 10px; }
  .brand-mark { width: 40px; height: 40px; border-radius: 50%; background: var(--orange); }
  .brand-name { font-family: "Dosis", sans-serif; font-weight: 600; font-size: 22px; color: var(--ink); }

  .hero { position: absolute; left: 0; top: 77px; width: 1200px; height: 486px; background: var(--orange); }

  .main-nav { position: absolute; left: 247px; top: 77px; display: flex; height: 40px; }
  .main-nav a { display: block; padding: 0 18px; font-size: 20px; font-weight: 500; color: var(--white); text-decoration: none; line-height: 56px; height: 40px; border-left: 1px solid rgba(255,255,255,.85); }
  .main-nav a:first-child { border-left: none; color: var(--ink); }

  .search-panel { position: absolute; left: 102px; top: 148px; width: 995px; height: 129px; background: var(--panel); border-radius: 8px; z-index: 3; }
  .search-panel-frame { position: absolute; left: 9px; top: 9px; right: 9px; bottom: 8px; border: 1px solid rgba(242,111,58,.55); }
  .search-title { position: absolute; left: 40px; top: 22px; white-space: nowrap; }
  .search-title strong { font-family: "Oswald", sans-serif; font-weight: 700; font-size: 29px; color: var(--white); letter-spacing: -0.5px; text-transform: uppercase; }
  .search-title span { font-family: "Dosis", sans-serif; font-weight: 500; font-size: 31px; color: var(--teal); margin-left: 14px; }
  .select { position: absolute; top: 74px; width: 261px; height: 33px; background: var(--white); border: 2px solid var(--orange); font-family: "Open Sans", sans-serif; font-size: 16px; color: var(--grey); line-height: 29px; padding-left: 9px; }
  .select svg { position: absolute; right: 10px; top: 10px; }
  .select-degree { left: 43px; }
  .select-category { left: 326px; }
  .select-subject { left: 610px; }
  .search-button { position: absolute; left: 877px; top: 70px; width: 100px; height: 38px; background: var(--teal-dark); border: 2px solid var(--orange); color: var(--white); font-family: "Open Sans", sans-serif; font-size: 16px; text-align: center; line-height: 34px; }

  .hero-photo { position: absolute; left: 40px; top: 268px; width: 760px; height: 295px; background: linear-gradient(90deg, rgba(242,111,58,0) 0%, var(--photo-light) 14%, var(--photo-mid) 45%, var(--photo-dark) 70%, rgba(242,111,58,0) 100%); }

  .tagline-circle { position: absolute; left: 754px; top: 237px; width: 344px; height: 344px; border-radius: 50%; background: var(--orange-soft); opacity: .9; }
  .tagline { position: absolute; left: 781px; top: 327px; font-family: "Oswald", sans-serif; font-weight: 600; font-size: 30px; line-height: 35px; color: var(--headline-dark); }

  .stats-band { position: absolute; left: 0; top: 563px; width: 1200px; height: 121px; background: var(--navy); }
  .bottom-edge { position: absolute; left: 0; top: 684px; width: 1200px; height: 5px; background: #e4e4e4; }
  .stat-bar { position: absolute; left: 104px; width: 172px; height: 38px; border: 1px solid var(--navy-line); }
  .stat-fill { position: absolute; left: 0; top: 0; width: 97px; height: 100%; background: var(--teal-dark); }
  .stat-value { position: absolute; left: 16px; top: 0; font-family: "Oswald", sans-serif; font-weight: 500; font-size: 26px; line-height: 36px; color: var(--white); }
  .stat-1996 { top: 579px; }
  .stat-2011 { top: 630px; }
  .stat-label { position: absolute; left: 295px; font-family: "Oswald", sans-serif; font-weight: 700; font-size: 20px; color: var(--orange); text-transform: uppercase; letter-spacing: -0.5px; }
  .label-1996 { top: 582px; }
  .label-2011 { top: 634px; }

  .debt-pie { position: absolute; left: 598px; top: 576px; }
  .debt-note { position: absolute; left: 690px; top: 581px; width: 400px; text-align: center; }
  .debt-note h2 { font-family: "Dosis", sans-serif; font-weight: 500; font-size: 18px; color: var(--orange); }
  .debt-note p { margin-top: 6px; font-family: "Open Sans", sans-serif; font-size: 12.5px; line-height: 17.5px; color: var(--white); padding: 0 20px; }
</style>
</head>
<body>
<div class="header">
  <div class="top-bar"></div>
  <div class="hero"></div>

  <div class="brand">
    <div class="brand-mark"></div>
    <div class="brand-name">Brightvale Learning Hub</div>
  </div>

  <nav class="main-nav">
    <a href="#">Home</a>
    <a href="#">Finacial Aid</a>
    <a href="#">Cost savings</a>
    <a href="#">Coleges</a>
    <a href="#">Awards</a>
    <a href="#">Blog</a>
    <a href="#">Contact Us</a>
  </nav>

  <div class="hero-photo" role="img" aria-label="Photo of a businessman in a suit crouched at the start line of a running track beside an open laptop"></div>

  <div class="tagline-circle"></div>
  <h1 class="tagline">Your #1 Resource<br>for an Affordable<br>Online College Education</h1>

  <form class="search-panel">
    <div class="search-panel-frame"></div>
    <div class="search-title"><strong>Your future is one step away</strong><span>Lets get start</span></div>
    <div class="select select-degree">Choose a Degree level
      <svg width="18" height="10" viewBox="0 0 18 10"><path d="M0 0H18L9 10Z" fill="#f26f3a"/></svg></div>
    <div class="select select-category">Choose a Category
      <svg width="18" height="10" viewBox="0 0 18 10"><path d="M0 0H18L9 10Z" fill="#f26f3a"/></svg></div>
    <div class="select select-subject">Choose a Subject
      <svg width="18" height="10" viewBox="0 0 18 10"><path d="M0 0H18L9 10Z" fill="#f26f3a"/></svg></div>
    <div class="search-button">Search</div>
  </form>

  <section class="stats-band"></section>
  <div class="bottom-edge"></div>

  <div class="stat-bar stat-1996"><div class="stat-fill"></div><div class="stat-value">$12,500</div></div>
  <div class="stat-label label-1996">Average student debt in 1996</div>
  <div class="stat-bar stat-2011"><div class="stat-fill"></div><div class="stat-value">$26,600</div></div>
  <div class="stat-label label-2011">Average student debt in 2011</div>

  <svg class="debt-pie" width="88" height="88" viewBox="0 0 88 88">
    <circle cx="44" cy="44" r="44" fill="#1b2328"/>
    <path d="M44 44 L44 0 A44 44 0 1 1 6.85 67.58 Z" fill="#0e5a55" transform="scale(-1,1) translate(-88,0)"/>
    <text x="44" y="52" text-anchor="middle" font-family="Oswald, sans-serif" font-weight="500" font-size="24" fill="#ffffff">66%</text>
  </svg>

  <div class="debt-note">
    <h2>College Costs Rising &amp; Student Debt Ballooning</h2>
    <p>Brightvale Learning Hub helps students find affordable college options and provides information about financial aid and college rankings.</p>
  </div>
</div>
</body>
</html>
```